Magical healing ointment looking for new branded labels

I need a new product label for my healing comfrey ointments, which started as just a simple ointment, and has grown to include a few varients including a body oil and lip balm. It sells quite well when I have a market, which I don't always have time to do - so I'd like to take it and leave it with some health shops, however for this I'd really like a more professional label to take these products further.

The company name is Brightwren Meadow - slogan Natural by Nature; as I am both a healer that makes ointments and yet also make scarves, cowls with high quality natural wool.
The ointment is simply called 'Comfrey Ointment', don't mind if it has Magical or healing in front of it. It's made by me, with high quality all natural, locally sourced organic ingredients, and supports the healing of bones, injuries, RSI, arthritis, rheuma, eczema, aches and pains.. Comfrey itself is an ancient herb also used in medieval herblore and by the ancient romans, so my keys words are to get feeling for the brand:
Timeless/ classic/ clean/ natural/ quality/ confident/ healing

I would like the labels to stand out, and look professional. The smallest size is 6 x 2.5 cm, this is an amber small jar of 30ml, the larger jar is double that size at 60ml, and the bottles bigger. I would like to be able to add a bit on the side if needed to add ingredients, and be able to scale the label up or down depending on the size of the jar. On top of this would like to be able to text as needed depending on the product in the jar.

Have included my company logo - for an idea of what that looks like, please note though that this branding or style doesn't need to include this logo, nor look like this logo. I've also included an example of someone who I think is doing a good job of being unique, simple, classic and appealing. Let me know if you have any questions. Thanks!

Target Market(s)

People with an eco-sustainable mind-set that are looking to resolve ailments naturally.

Industry/Entity Type

Health

Requirements
Must have
• The product name, and company name
Nice to have
• I'd like to leave most of the design to the designers ideas, however am ok to have leaves - or natural elements that support the typography, but not overwhelm it.

```html
<!DOCTYPE html>
<html lang="en">
<head>
<meta charset="utf-8">
<title>Brightwren Meadow – Healing Comfrey Ointment Label</title>
<link href="https://fonts.googleapis.com/css2?family=Dancing+Script:wght@500&family=Gelasio:wght@400&family=Open+Sans:wght@400&display=swap" rel="stylesheet">
<style>
  :root {
    --page-bg: #f3f1ee;
    --label-bg: #ffffff;
    --brand-ink: #3b2f4a;
    --title-ink: #3a3530;
    --rule-red: #6e2a2a;
    --ornament-ink: #2a2a2a;
    --band-green: #1f6a24;
    --band-text: #ffffff;
  }
  * { margin: 0; padding: 0; box-sizing: border-box; }
  html, body {
    width: 1200px;
    height: 1200px;
    overflow: hidden;
    background: var(--page-bg);
  }
  .canvas {
    position: relative;
    width: 1200px;
    height: 1200px;
  }
  .label {
    position: absolute;
    left: 50px;
    top: 205px;
    width: 1100px;
    height: 790px;
    background: var(--label-bg);
    box-shadow: 0 2px 10px rgba(0,0,0,0.08);
  }
  .brand-name {
    position: absolute;
    top: 48px;
    left: 0;
    width: 100%;
    text-align: center;
    font-family: "Dancing Script", cursive;
    font-weight: 500;
    font-size: 70px;
    color: var(--brand-ink);
    line-height: 1;
  }
  .divider {
    position: absolute;
    top: 165px;
    left: 0;
    width: 100%;
    height: 44px;
  }
  .product-title {
    position: absolute;
    top: 278px;
    left: 0;
    width: 100%;
    text-align: center;
    font-family: "Gelasio", serif;
    font-weight: 400;
    font-size: 94px;
    line-height: 134px;
    color: var(--title-ink);
  }
  .quality-band {
    position: absolute;
    top: 580px;
    left: 0;
    width: 100%;
    height: 178px;
    background: var(--band-green);
    display: flex;
    flex-direction: column;
    justify-content: center;
    align-items: center;
    font-family: "Open Sans", sans-serif;
    font-size: 40px;
    line-height: 1.35;
    letter-spacing: 0.5px;
    color: var(--band-text);
    text-align: center;
  }
</style>
</head>
<body>
  <main class="canvas">
    <section class="label">
      <div class="brand-name">Brightwren Meadow</div>

      <svg class="divider" viewBox="0 0 1100 44" xmlns="http://www.w3.org/2000/svg">
        <line x1="0" y1="22" x2="395" y2="22" stroke="var(--rule-red)" stroke-width="3"/>
        <line x1="705" y1="22" x2="1100" y2="22" stroke="var(--rule-red)" stroke-width="3"/>
        <rect x="425" y="10" width="250" height="24" rx="12" fill="var(--ornament-ink)" opacity="0.85" role="img" aria-label="Decorative scroll flourish centred between the rules"/>
      </svg>

      <h1 class="product-title">Healing<br>Comfrey Ointment</h1>

      <div class="quality-band">
        <span>HIGH QUALITY ALL NATURAL, LOCALLY SOURCED</span>
        <span>ORGANIC INGREDIENTS</span>
      </div>
    </section>
  </main>
</body>
</html>
```